Employee Wellbeing Model Graphic Design

A visual/graphic representation of our Employee Wellbeing model.
Our model is a combination of the Ara Kōrero Ahi model of health and wellbeing and the wellbeing continuum.
We would like the visual to be on one page. The design should be modern and simple.
The powerpoint attached shows the information we are wanting to share with our employees about our wellbeing programme.

Target Market(s)

Our employees

Industry/Entity Type

Event Management

Font styles to use
Sans Serif
Other font styles liked:
• calibri light

Colors
00AB8E
00BBA5
67D7C9
C6EFE9
E9F9F6

```html
<!DOCTYPE html>
<html lang="en">
<head>
<meta charset="utf-8">
<title>Our Wellbeing Framework</title>
<link rel="stylesheet" href="https://fonts.googleapis.com/css2?family=Carlito:ital,wght@0,400;0,700;1,400&family=Open+Sans:wght@600;700&display=swap">
<style>
:root{
  --teal:#0DB9A5;
  --teal-dark:#00AB8E;
  --teal-mid:#67D7C9;
  --teal-pale:#C6EFE9;
  --teal-mist:#E9F9F6;
  --ink:#1d1d1d;
  --grey:#555;
  --unwell:#E8245F;
  --struggling:#F6A04D;
  --going-ok:#D7C23A;
  --thriving:#5BB562;
  --page:#ffffff;
}
*{box-sizing:border-box;margin:0;padding:0}
html,body{width:893px;height:1200px;overflow:hidden;background:var(--page)}
body{font-family:"Carlito",Calibri,sans-serif;color:var(--ink);position:relative}
.abs{position:absolute}

/* header */
.header-band{left:0;top:0;width:633px;height:85px}
.title{left:64px;top:26px;font-family:"Open Sans",sans-serif;font-weight:700;font-size:30.5px;color:#fff;line-height:1;white-space:nowrap}
.brand{left:660px;top:36px;width:200px;text-align:center;font-family:"Open Sans",sans-serif;font-weight:700;font-size:22px;line-height:28px;color:var(--teal);white-space:nowrap}

/* model */
.model-art{left:30px;top:117px;width:262px;height:161px;background:var(--teal-pale);border-radius:4px}
.model-title{left:309px;top:104px;font-family:"Open Sans",sans-serif;font-weight:700;font-size:20px;color:var(--grey);white-space:nowrap}
.model-intro{left:309px;top:135px;width:532px;font-size:14.2px;line-height:17.3px}
.pill{height:18px;width:174px;background:var(--teal);color:#fff;font-weight:700;font-size:12px;line-height:18px;padding-left:9px;border-radius:4px}
.pill-note{font-style:italic;font-size:12px;color:#333}

/* continuum */
.stage{top:312px;font-family:"Open Sans",sans-serif;font-weight:700;font-size:10.5px;transform:translateX(-50%)}
.stage--unwell{left:197px;color:var(--unwell)}
.stage--struggling{left:388px;color:var(--struggling)}
.stage--ok{left:583px;color:var(--going-ok)}
.stage--thriving{left:777px;color:var(--thriving)}
.spectrum{left:110px;width:751px;height:11px;border-radius:6px;background:linear-gradient(90deg,var(--unwell) 0%,var(--struggling) 35%,#E3BE3A 58%,#CFC93A 72%,var(--thriving) 100%)}

.side-tab{left:0;width:81px;background:var(--teal)}
.tab-1{top:331px;height:251px;border-bottom-right-radius:16px}
.tab-3{top:889px;height:311px;border-top-right-radius:16px}
.side-label{left:0;width:81px;display:flex;justify-content:center;align-items:center}
.side-label .vt{writing-mode:vertical-rl;transform:rotate(180deg);text-align:center;font-weight:700;font-size:15px;line-height:17px}
.side-label .vt em{display:block;font-weight:400;font-style:italic}
.on-teal{color:#fff}
.on-white{color:var(--teal)}

.lede{left:112px;width:748px;font-style:italic;font-size:12.2px;line-height:15.3px}
.col{font-size:12.1px;line-height:15.3px;list-style:none}
.col li{position:relative;padding-left:10px}
.col li::before{content:"•";position:absolute;left:0}

.approach{font-size:12.2px;line-height:15.3px;white-space:nowrap}
.approach b{display:block;color:var(--teal);font-weight:700}
.programme-title{left:484px;top:985px;transform:translateX(-50%);white-space:nowrap;font-family:"Open Sans",sans-serif;font-weight:700;font-size:14.5px;color:var(--teal)}
.programme-art{left:84px;top:992px;width:319px;height:208px;background:var(--teal-mist);opacity:.7}
</style>
</head>
<body>

<svg class="abs header-band" viewBox="0 0 633 85" aria-hidden="true"><polygon points="0,0 633,0 597,85 0,85" fill="#0DB9A5"/></svg>
<h1 class="abs title">OUR WELLBEING FRAMEWORK</h1>
<div class="abs brand">Kahu Events</div>

<div class="abs model-art" role="img" aria-label="Illustration of a meeting house representing the Ara Kōrero Ahi model"></div>
<h2 class="abs model-title">ARA KŌRERO AHI</h2>
<p class="abs model-intro">When all these things are in balance, we thrive. When one or more of these is out of balance our wellbeing is impacted. By aligning workplace activities with Ara Kōrero Ahi, organizations can create an environment where well-being is valued, and employees thrive</p>

<div class="abs pill" style="left:312px;top:211px">TAHA HINESARE</div>
<div class="abs pill-note" style="left:312px;top:233px">▪ Mental/Emotional Heath</div>
<div class="abs pill" style="left:491px;top:211px">TAHA WHANAU</div>
<div class="abs pill-note" style="left:491px;top:233px">▪ Family/Community Health</div>
<div class="abs pill" style="left:671px;top:211px">WHENUA</div>
<div class="abs pill-note" style="left:671px;top:233px">▪ Land/Roots</div>
<div class="abs pill" style="left:312px;top:255px">TANA TINANA</div>
<div class="abs pill-note" style="left:312px;top:277px">▪ Physical Health</div>
<div class="abs pill" style="left:491px;top:255px">TAHA WAIRUA</div>
<div class="abs pill-note" style="left:491px;top:277px">▪ Spiritual Health</div>

<div class="abs stage stage--unwell">UNWELL</div>
<div class="abs stage stage--struggling">STRUGGLING</div>
<div class="abs stage stage--ok">GOING OK</div>
<div class="abs stage stage--thriving">THRIVING</div>
<div class="abs spectrum" style="top:331px"></div>

<!-- continuum -->
<div class="abs side-tab tab-1"></div>
<div class="abs side-label" style="top:331px;height:251px"><div class="vt on-teal">The Wellbeing Continuum</div></div>
<p class="abs lede" style="top:350px">People can have a range of mental health experiences across the continuum that will change over time. It is usual to cycle across the Thriving and Going Ok parts of the spectrum.</p>
<ul class="abs col" style="left:117px;top:388px;width:162px">
  <li>People who are mentally unwell and/or have a diagnosed mental illness</li>
  <li>Severe and persistent functional impairment</li>
  <li>Neurochemical process outside of the individuals’ control is often established</li>
</ul>
<ul class="abs col" style="left:302px;top:388px;width:182px">
  <li>People who don’t meet the criteria for a diagnosable mental illness, but who may be highly stressed or distressed</li>
  <li>More severe and persistent functional impairment</li>
  <li>A mental health problem develops</li>
  <li>Usual coping mechanisms may not suffice or don’t have the same impact</li>
</ul>
<ul class="abs col" style="left:493px;top:388px;width:206px">
  <li>People who lack general mental wellbeing and a sense of being reasonably happy with life</li>
  <li>Often show as disengaged and unmotivated, lack meaning and purpose in their daily lives</li>
  <li>Likely to have higher rates of physical illness and workplace accidents</li>
  <li>People develop coping mechanisms which can be applied to help revert to full mental health – thriving</li>
</ul>
<ul class="abs col" style="left:702px;top:388px;width:156px">
  <li>People who are mentally unwell and/or have a diagnosed mental illness</li>
  <li>Severe and persistent functional impairment</li>
  <li>Neurochemical process outside of the individuals’ control is often established</li>
</ul>

<!-- signs -->
<div class="abs side-label" style="top:598px;height:254px"><div class="vt on-white">The Wellbeing Continuum<em>Signs and Symptoms</em></div></div>
<p class="abs lede" style="top:592px">People can have a range of mental health experiences across the continuum that will change over time. It is usual to cycle across the Thriving and Going Ok parts of the spectrum</p>
<ul class="abs col" style="left:117px;top:630px;width:182px">
  <li>Angry outbursts/aggression</li>
  <li>Excessive anxiety/panic attacks</li>
  <li>Thoughts of suicide</li>
  <li>Can’t perform duties, control behaviour or concentrate</li>
  <li>Can’t fall asleep or stay asleep</li>
  <li>Sleeping too much or too little</li>
  <li>Physical illness</li>
  <li>Constant fatigue</li>
  <li>Not going out/answering phone</li>
  <li>Substance or gambling addiction</li>
  <li>Other addictions</li>
</ul>
<ul class="abs col" style="left:302px;top:630px;width:182px">
  <li>Anger</li>
  <li>Anxiety</li>
  <li>Pervasively sad/hopeless</li>
  <li>Negative attitude</li>
  <li>Poor performance/workaholic</li>
  <li>Poor concentration/decisions</li>
  <li>Restless disturbed sleep</li>
  <li>Recurrent images/nightmares</li>
  <li>Increased aches and pains</li>
  <li>Increased fatigue</li>
  <li>Avoidance</li>
  <li>Withdrawal</li>
  <li>Increased substance use/gambling hard to control</li>
</ul>
<ul class="abs col" style="left:493px;top:630px;width:192px">
  <li>Irritable/impatient</li>
  <li>Nervous</li>
  <li>Sadness/overwhelmed</li>
  <li>Procrastination</li>
  <li>Forgetfulness</li>
  <li>Trouble sleeping</li>
  <li>Intrusive thoughts</li>
  <li>Nightmares</li>
  <li>Muscle tension/headaches</li>
  <li>Low energy</li>
  <li>Decreased activity/ socialising</li>
  <li>Regular but controlled substance use or gambling</li>
</ul>
<ul class="abs col" style="left:702px;top:630px;width:156px">
  <li>Normal mood fluctuations</li>
  <li>Calm and takes things in stride</li>
  <li>Good sense of humour</li>
  <li>Performing well</li>
  <li>In control mentally</li>
  <li>Normal sleep patterns</li>
  <li>Few sleep difficulties</li>
  <li>Physically well</li>
  <li>Good energy levels</li>
  <li>Physically and socially active</li>
  <li>Not using substances to cope</li>
  <li>None or limited gambling</li>
</ul>

<div class="abs spectrum" style="top:876px"></div>

<!-- initiatives -->
<div class="abs side-tab tab-3"></div>
<div class="abs programme-art" role="img" aria-label="Faint meeting house illustration in the background"></div>
<div class="abs side-label" style="top:889px;height:311px"><div class="vt on-teal">Applying the Wellbeing Continuum<em>Our Wellbeing Initiatives</em></div></div>
<p class="abs lede" style="top:895px">Our approach is to provide a programme of wellbeing interventions across the continuum, and ensure our initiatives align with the Ara Kōrero Ahi model by providing support for physical health, mental/emotional health, family and community health, spiritual health and connection to whenua.</p>
<div class="abs approach" style="left:112px;top:947px"><b>Treatment</b>Providing Help, Supporting Recovery</div>
<div class="abs approach" style="left:355px;top:947px"><b>Building Capability</b>Changing Mindsets, Raising Awareness</div>
<div class="abs approach" style="left:621px;top:947px"><b>Prevention</b>Reducing Risks, Staying Well</div>
<h3 class="abs programme-title">OUR PROGRAMME OF WELLBEING INITIATIVES</h3>
<ul class="abs col" style="left:117px;top:1010px;width:215px">
  <li>Staff Counselling Service</li>
  <li>Domestic Violence Leave</li>
  <li>Injury Management (Kinetic Health)</li>
  <li>Psychological First Aiders</li>
</ul>
<ul class="abs col" style="left:358px;top:1010px;width:230px">
  <li>Wellbeing Intranet Site</li>
  <li>Wellbeing Training Module in Kōwhai Learn</li>
  <li>Lend a Hand (volunteer) Day</li>
  <li>Positive Leadership Programme</li>
  <li>Regular Staff Engagement Activities</li>
  <li>Wellbeing Campaigns</li>
  <li>Culture Committee</li>
  <li>Clear Heads e-learning for Managers</li>
</ul>
<ul class="abs col" style="left:625px;top:1010px;width:232px">
  <li>Wellness Days</li>
  <li>Annual Health Monitoring</li>
  <li>Flu Vaccinations</li>
  <li>Bullying &amp; Harassment Prevention Policy</li>
  <li>Flexible Work Options</li>
  <li>Fatigue Management Guidelines</li>
  <li>Recreation Leave Purchase</li>
  <li>Health and Wellbeing Policy</li>
  <li>Sick leave available from day 1 of employment</li>
  <li>RideLink for Business</li>
</ul>

</body>
</html>
```